Restaurant website built on Kelvo’s responsive platform- No coding skills needed

We are looking to add to our company's website www.kelvoweb.example a new inspiration page that will include examples of sites built using Kelvo's platform.
In order to make it relevant, we would like to have multiple choices for every category, one of the categories is “restaurants.”

REQUIREMENTS:
o Build a "fake" restaurant site on Kelvo’s responsive platform, no real restaurant information is needed. The site will include:
1. Homepage
• Restaurant header (no logo)
• Paragraph about the restaurant (can be Lorem ipsum)
• Contact details and contact buttons
• Chowrate reviews
• Reserve-a-table widget
• Open hours
2. Menu page
• You can use any menu you'd like
• Reserve a table widget
• Photo gallery
3. Footer
• Social Media links
• Map with location of restaurant

* Order of the elements is up to the designer
* Designer may add more elements as they see fit
* Designer may alter elements from page to page
* Designer will define the site color pallet and text style

****Learn more on how to create a website on Kelvo's platform here
https://clipvault.example/384920176

INSTRUCTIONS FOR THIS PROJECT:
Register for a 30-day free trial for Pro access to the platform:
http://www.kelvoweb.example/kelvopro?_dm_referral=PixHub

a. After registering, access the dashboard and click on “Create Responsive Website.”
b. Choose a template
c. Start editing! .
d. No need to publish. When ready, take a screenshot of the preview and submit the screenshot to this PixelHive project. Include the URL/Link to the preview within the submission description.
e. For more information on Kelvo, visit the support page at https://support.kelvoweb.example/02KelvoOne/Quick_Guide OR call our Support line Mon.-Fri., 9AM-9PM ET.1-866-555-0142

DESIGN PREFERENCES
freestyle (not related to the Kelvo brand)

DESIGN SAMPLES (for inspiration)
http://www.kelvoweb.example/responsive-website/templates

What not to include in the design -
no restrictions

DELIVERABLES:
* Website on Kelvo (No PSD. No coding needed)
* Screenshot preview to PixelHive with URL/link to your site’s preview.

ABOUT THE COMPANY:
Kelvo is a website builder based in California that allow designers, web designers and practically anyone to build its own site. No development and/or technical skills required.

NOTE:
* Kelvo is an external site and is not part of PixelHive
* Please refer to Kelvo's Terms and Conditions for information regarding how submissions will be handled (http://www.kelvoweb.example/legal/terms)

Target Market(s)

SMBs and web designers that want to create simple, professional and beautiful websites

Industry/Entity Type

Restaurant

Number of Pages Required

2 page

Requirements
Must have
• Please send a preview of the site you created on Kelvo, NOT a PSD/JPEG
Should not have
• No coding skills are needed- any web designer can build a site on Kelvo

```html
<!DOCTYPE html>
<html lang="en">
<head>
<meta charset="utf-8">
<title>Emberhall restaurant</title>
<link rel="stylesheet" href="https://fonts.googleapis.com/css2?family=Alegreya:wght@400;700&family=Niconne&display=swap">
<style>
  :root {
    --panel: rgba(38, 20, 12, 0.88);
    --bg-dark: #1f140d;
    --bg-mid: #4a3322;
    --bg-warm: #7a5a3a;
    --text: #e6ddd2;
    --text-soft: #d8cbb9;
    --title: #c9d6de;
    --accent: #e3874f;
    --rule: #cfc4b6;
    --frame: #cfcac4;
    --social-a: #4f6fb4;
    --social-b: #4fb0e0;
    --social-c: #d9503f;
  }
  * { box-sizing: border-box; margin: 0; padding: 0; }
  html, body { width: 1200px; height: 900px; overflow: hidden; }
  body {
    position: relative;
    font-family: "Alegreya", Georgia, serif;
    color: var(--text);
    background: var(--bg-dark);
  }
  .backdrop {
    position: absolute; inset: 0;
    background:
      radial-gradient(ellipse at 50% 35%, var(--bg-warm) 0%, transparent 55%),
      linear-gradient(90deg, var(--bg-dark) 0%, var(--bg-mid) 20%, #6b4e33 50%, var(--bg-mid) 80%, var(--bg-dark) 100%);
  }
  .site-nav {
    position: absolute; top: 10px; left: 606px;
    display: flex; gap: 21px;
  }
  .site-nav a {
    color: #fff; text-decoration: none;
    font-weight: 700; font-size: 16px;
    padding-bottom: 4px;
  }
  .site-nav a.is-active { border-bottom: 1px solid #fff; }
  .content-panel {
    position: absolute; left: 309px; top: 84px;
    width: 563px; height: 816px;
    background: var(--panel);
  }
  .hero-photo {
    position: absolute; left: 41px; top: 38px;
    width: 480px; height: 320px;
    border: 3px solid var(--frame);
    background: linear-gradient(120deg, #6b3a1c 0%, #b2502a 35%, #8a9a3a 60%, #d9d2b8 100%);
  }
  .restaurant-name {
    position: absolute; left: 0; width: 100%; top: 378px;
    text-align: center;
    font-family: "Niconne", cursive;
    font-size: 32px; color: var(--title);
  }
  .divider {
    position: absolute; left: 41px; top: 441px;
    width: 480px; height: 1px; background: var(--rule);
  }
  .info-col { position: absolute; top: 468px; }
  .info-col h2 {
    font-weight: 400; font-size: 22px; color: var(--text);
    margin-bottom: 12px;
  }
  .info-col p {
    font-size: 10.5px; line-height: 19px; color: var(--text-soft);
  }
  .col-contact { left: 41px; width: 150px; }
  .col-about { left: 205px; width: 150px; }
  .col-hours { left: 368px; width: 150px; }
  .read-more {
    display: block; text-align: right;
    color: var(--text); font-size: 10.5px; text-decoration: underline;
    margin-top: 2px;
  }
  .hours-row {
    display: flex; justify-content: space-between;
    font-size: 10.5px; line-height: 19px; color: var(--text-soft);
    margin-bottom: 8px;
  }
  .hours-row .time { width: 72px; text-align: right; }
  .hours-row .day-hi { color: var(--accent); }
  .location-map {
    position: absolute; left: 41px; top: 656px;
    width: 233px; height: 129px;
    background: linear-gradient(135deg, #a9c7e6 0%, #e9e5da 30%, #f2efe6 60%, #bfd7ee 100%);
  }
  .social-links {
    position: absolute; left: 288px; top: 656px;
    display: flex; gap: 9px;
  }
  .social-links span {
    display: block; width: 26px; height: 26px; border-radius: 4px;
  }
  .social-a { background: var(--social-a); }
  .social-b { background: var(--social-b); }
  .social-c { background: var(--social-c); }
  .company-name {
    position: absolute; left: 41px; top: 796px;
    font-size: 10.5px; color: var(--text-soft);
  }
</style>
</head>
<body>
  <div class="backdrop" role="img" aria-label="Photo of a dim restaurant interior with wooden beams and woven hanging lamps"></div>

  <nav class="site-nav">
    <a href="#" class="is-active">Home</a>
    <a href="#">Gallery</a>
    <a href="#">About Us</a>
    <a href="#">Contact</a>
  </nav>

  <main class="content-panel">
    <div class="hero-photo" role="img" aria-label="Photo of grilled meat and pepper skewers with a fresh salad and dip"></div>
    <h1 class="restaurant-name">Emberhall restaurant</h1>
    <div class="divider"></div>

    <section class="info-col col-contact">
      <h2>Get In Touch</h2>
      <p>Address: Street Address, City, State and Zip</p>
      <p>Mail: hello@emberhall.example</p>
      <p>Phone: 555-555-5555</p>
    </section>

    <section class="info-col col-about">
      <h2>About Us</h2>
      <p>Is a very fancy restaurant Where all the health and wonderful meals......</p>
      <a class="read-more" href="#">Read More &gt;</a>
    </section>

    <section class="info-col col-hours">
      <h2>Opening Hours</h2>
      <div class="hours-row"><span>Mon - <span class="day-hi">Fri</span></span><span class="time">9:00 am - 7:00 pm</span></div>
      <div class="hours-row"><span>Saturday</span><span class="time">10:00 am - 6:00 pm</span></div>
      <div class="hours-row"><span>Sunday</span><span class="time">Closed</span></div>
    </section>

    <div class="location-map" role="img" aria-label="Street map showing the restaurant location with a red pin"></div>

    <div class="social-links">
      <span class="social-a" role="img" aria-label="Friendbook"></span>
      <span class="social-b" role="img" aria-label="Chirper"></span>
      <span class="social-c" role="img" aria-label="Circleplus"></span>
    </div>

    <p class="company-name">Company Name</p>
  </main>
</body>
</html>
```